Business Card Re-Design/Update

We'd like to update out business cards. I've included our current "Style guide" which has the colour scheme of the organisation in it. I've also included the branding files with logos etc in them.

I've also included a copy of one of our existing cards so that you can see how ugly/dated they look. I'd like a fresh modern corporate look.

Target Market(s)

These are for our clients, potential clients, industry contacts - like all business cards

Contact Information for Business Card

Name
Position
Company Address - Level 1, 47 Garnet Lane, Toowong Qld 4066
Direct Phone
mobile
Email
Website -www.korvalnet.com.au
Logo

Colors

Designer to choose colors to be used in the design.

Requirements
Must have
• Main Logo
• Cards will need to be editable to be able to personalize them for each new employee.
Nice to have
• The MapOUT, HandOVER, UpKEEP would be okay to have if they can be sensibly and professionally added to the look without detracting from the main imagery.
• Maybe they could go on the back of the card? will leave this to your creative discretion as to whether/where they fit.
Should not have
• Should not have decorative or script fonts

```html
<!DOCTYPE html>
<html lang="en">
<head>
<meta charset="utf-8">
<title>Korvalnet Business Card</title>
<link rel="stylesheet" href="https://fonts.googleapis.com/css2?family=Arimo:wght@400;700&display=swap">
<style>
  :root {
    --stage: #2b2321;
    --card-black: #0d0d0e;
    --card-black-soft: #161617;
    --brand-red: #d8161f;
    --brand-white: #ffffff;
    --text-light: #e6e6e6;
    --text-muted: #bdbdbd;
    --rule: #4a4a4a;
    --logo-grey: #d9d9d9;
  }
  * { box-sizing: border-box; margin: 0; padding: 0; }
  html, body {
    width: 1200px; height: 842px; overflow: hidden;
    background: var(--stage);
    font-family: "Arimo", Arial, sans-serif;
  }
  .canvas {
    position: relative; width: 1200px; height: 842px;
    display: flex; align-items: center; justify-content: center; gap: 60px;
  }
  .card {
    position: relative; width: 520px; height: 318px;
    background: linear-gradient(160deg, var(--card-black-soft), var(--card-black));
    overflow: hidden;
    box-shadow: 0 14px 30px rgba(0,0,0,.45);
  }

  /* Back: contact side */
  .card-back .band {
    position: absolute; left: 0; right: 0; height: 12px; background: var(--brand-red);
  }
  .card-back .band-top { top: 8px; }
  .card-back .band-bottom { bottom: 8px; }
  .contact {
    position: absolute; left: 0; right: 0; top: 46px;
    text-align: center; color: var(--text-light);
  }
  .contact-name {
    color: var(--brand-red); font-weight: 700; font-size: 19px; letter-spacing: .2px;
  }
  .contact-position { font-size: 14px; margin-top: 4px; }
  .rule {
    width: 240px; height: 1px; background: var(--rule); margin: 10px auto;
  }
  .icon-row { display: flex; justify-content: center; gap: 5px; margin-bottom: 6px; }
  .icon-row svg { width: 11px; height: 11px; fill: var(--brand-red); }
  .contact-lines { font-size: 14px; line-height: 20px; }
  .contact-address { font-size: 14.5px; margin-top: 14px; }

  /* Front: brand side */
  .tab {
    position: absolute; width: 34px; height: 46px; background: var(--brand-red);
  }
  .tab::after {
    content: ""; position: absolute; top: 0; bottom: 0; width: 5px; background: var(--brand-white);
  }
  .tab-left { left: 0; top: 122px; }
  .tab-left::after { right: 0; }
  .tab-right { right: 0; top: 36px; }
  .tab-right::after { left: 0; }
  .brand {
    position: absolute; left: 0; right: 0; top: 50%; transform: translateY(-50%);
    display: flex; align-items: center; justify-content: center; gap: 14px;
  }
  .brand-mark { width: 34px; height: 34px; background: var(--brand-red); }
  .brand-name {
    font-weight: 700; font-size: 46px; color: var(--logo-grey); letter-spacing: -.5px;
  }
</style>
</head>
<body>
<main class="canvas">

  <section class="card card-back" aria-label="Business card back, contact details">
    <div class="band band-top"></div>
    <div class="contact">
      <p class="contact-name">Daniel Hartley</p>
      <p class="contact-position">Position</p>
      <div class="rule"></div>
      <div class="icon-row" aria-hidden="true">
        <svg viewBox="0 0 12 12"><rect x="3" y="0.5" width="6" height="11" rx="1.2"/><rect x="4.2" y="2" width="3.6" height="6.5" fill="#0d0d0e"/></svg>
        <svg viewBox="0 0 12 12"><path d="M2.2 1h2.2l1 2.6-1.3 1a6 6 0 0 0 3.3 3.3l1-1.3 2.6 1v2.2c0 .7-.5 1.2-1.2 1.2A9.8 9.8 0 0 1 1 2.2C1 1.5 1.5 1 2.2 1z"/></svg>
        <svg viewBox="0 0 12 12"><rect x="0.5" y="2" width="11" height="8" rx="1"/><path d="M1 2.6 6 6.6l5-4" fill="none" stroke="#0d0d0e" stroke-width="1"/></svg>
        <svg viewBox="0 0 12 12"><circle cx="6" cy="6" r="5.5"/><path d="M0.8 6h10.4M6 0.6c-2.6 3-2.6 7.8 0 10.8M6 0.6c2.6 3 2.6 7.8 0 10.8" fill="none" stroke="#0d0d0e" stroke-width=".8"/></svg>
      </div>
      <div class="contact-lines">
        <p>484 210 36718</p>
        <p>484 210 36718</p>
        <p>hello@korvalnet.com.au</p>
        <p>www.korvalnet.com.au</p>
      </div>
      <div class="rule"></div>
      <p class="contact-address">Level 1, 47 Garnet Lane, Toowong Qld 4066</p>
    </div>
    <div class="band band-bottom"></div>
  </section>

  <section class="card card-front" aria-label="Business card front, brand">
    <div class="tab tab-right"></div>
    <div class="tab tab-left"></div>
    <div class="brand">
      <span class="brand-mark" aria-hidden="true"></span>
      <span class="brand-name">korvalnet</span>
    </div>
  </section>

</main>
</body>
</html>
```